Business card on Pvc transparent frosted

I need a business advertising card that will be eye catching and fun.
Target Market(s)
Rednecks, country, hunters, Fisherman, ATV users, lifted trucks, cowboys, cattle ranchers, farmers, etc
Industry/Entity Type
Apparel Store
Contact Information for Business Card
This will he printed on single side of a transparent frosted plastic card with shinny foil print option.
Requirements
Must have
- 1 - My logo.
- 2 - HOLLER BOOTSTRAP OUTFITTERS
- 3 - my motto "DONT judge how we look..... Judge the WILD mess we make!!"; 4 - my website "hollerbootstrap@mailvex.example"

Nice to have
- Use your imagination with negative space, partial graffics, etc. Keep in mind you can kind of see through the card

Should not have
- Do not change colors of chevrons

```html
<!DOCTYPE html>
<html lang="en">
<head>
<meta charset="utf-8">
<title>Holler Bootstrap Outfitters – Business Card</title>
<link rel="stylesheet" href="https://fonts.googleapis.com/css2?family=Arimo:wght@400;700&display=swap">
<style>
  :root {
    --page-bg: #e9e6e2;
    --card-frost: #eeeae6;
    --red-deep: #c40d12;
    --red-bright: #e3262a;
    --gold: #e0a21b;
    --ink: #2a1a1a;
    --ink-soft: #3b2424;
    --name-white: #f4eeee;
    --notch: #262626;
  }
  * { box-sizing: border-box; margin: 0; padding: 0; }
  html, body {
    width: 1200px; height: 970px; overflow: hidden;
    background: var(--page-bg);
    font-family: "Arimo", Arial, sans-serif;
  }
  .card {
    position: absolute; left: 80px; top: 189px;
    width: 1040px; height: 592px;
  }
  .card-shape { position: absolute; inset: 0; }
  .contact {
    position: absolute; left: 70px; top: 100px;
    color: var(--ink);
  }
  .person-name {
    font-size: 31px; font-weight: 700; color: var(--name-white);
    letter-spacing: 0.5px; line-height: 34px;
  }
  .person-role { font-size: 24px; line-height: 26px; color: var(--ink-soft); }
  .address { margin-top: 32px; font-size: 24px; line-height: 38px; }
  .channels { margin-top: 20px; list-style: none; font-size: 24px; line-height: 35px; }
  .channels li { display: flex; align-items: center; gap: 12px; }
  .channels svg { width: 22px; height: 22px; flex: none; }
  .motto { margin-top: 20px; font-size: 24px; line-height: 33px; }
  .brand {
    position: absolute; left: 640px; top: 230px; width: 300px;
    display: flex; flex-direction: column; align-items: center; gap: 18px;
  }
  .brand-dot {
    width: 46px; height: 46px; border-radius: 50%; background: var(--red-deep);
  }
  .brand-name {
    font-size: 26px; font-weight: 700; color: var(--ink);
    text-align: center; line-height: 32px; letter-spacing: 1px;
  }
</style>
</head>
<body>
  <div class="card">
    <svg class="card-shape" viewBox="0 0 1040 592" width="1040" height="592">
      <defs>
        <linearGradient id="redPanel" x1="0" y1="0" x2="1" y2="1">
          <stop offset="0" stop-color="var(--red-bright)"/>
          <stop offset="0.5" stop-color="var(--red-deep)"/>
          <stop offset="1" stop-color="#b51e22"/>
        </linearGradient>
        <clipPath id="cardClip"><rect width="1040" height="592" rx="22"/></clipPath>
      </defs>
      <g clip-path="url(#cardClip)">
        <rect class="frost" width="1040" height="592" fill="var(--card-frost)"/>
        <path class="gold-arc" d="M548 0 Q470 296 548 592" fill="none" stroke="var(--gold)" stroke-width="6"/>
        <path class="red-panel" d="M0 0 H540 Q462 296 540 592 H0 Z" fill="url(#redPanel)"/>
        <circle class="notch" cx="0" cy="133" r="30" fill="var(--notch)"/>
      </g>
    </svg>

    <div class="contact">
      <p class="person-name">JOHN SMITH</p>
      <p class="person-role">Director</p>
      <p class="address">PO BOX 123 your address<br>2nd street Melbourne</p>
      <ul class="channels">
        <li>
          <svg viewBox="0 0 22 22"><rect x="6" y="2" width="10" height="18" rx="2" fill="none" stroke="var(--ink)" stroke-width="2"/><circle cx="11" cy="16.5" r="1.2" fill="var(--ink)"/></svg>
          (123) 456-7890
        </li>
        <li>
          <svg viewBox="0 0 22 22"><rect x="2" y="5" width="18" height="13" fill="none" stroke="var(--ink)" stroke-width="2"/><path d="M2 5 L11 12 L20 5" fill="none" stroke="var(--ink)" stroke-width="2"/></svg>
          hollerbootstrap@mailvex.example
        </li>
        <li>
          <svg viewBox="0 0 22 22"><circle cx="11" cy="11" r="9" fill="none" stroke="var(--ink)" stroke-width="1.8"/><ellipse cx="11" cy="11" rx="4" ry="9" fill="none" stroke="var(--ink)" stroke-width="1.5"/><path d="M2 11 H20 M4 6 H18 M4 16 H18" stroke="var(--ink)" stroke-width="1.3"/></svg>
          hollerbootstrap.example
        </li>
      </ul>
      <p class="motto">DONT judge how we look.....<br>Judge the WILD mess we make!!</p>
    </div>

    <div class="brand">
      <span class="brand-dot"></span>
      <p class="brand-name">HOLLER BOOTSTRAP<br>OUTFITTERS</p>
    </div>
  </div>
</body>
</html>
```